International online gaming platform needs a game UI design

1. We need a game interface for three kinds of theme based on our guideline and sample mockup.
2. The product type is the online casino games related, we need a series of casino games UIs, however, we can start on the game lobby first.
3. Three theme you might choose from or refer to:
A. 3D look & feel
B. Realistic casino theme
C. Richness and grandeur
D. European casino style
4. NOT ALLOWED to change the design layout.
MUST follow our sample mock up and ONLY redefine the design style.
5. All items must be in a stand-alone component, eg. Button, Tab, Icon,... etc.
6. We need the layout in vector shape, but we can review in JPG or PNG format.
7. The image size: 1366 x 768

Updated:
1. All items and their positions should be same as the sample UI we provided.
Please redesign all the items and create a new theme for it.
No need to create a new layout.
2. Although we accept the draft design, but all the items in UI should be completed.
3. All the wordings in the sample UI are confirmed, you might change the fonts.
4. For the avatar in the left hand side, you don't have to redraw it.
We already have our own avatar system implemented.
5. All the items such as icons, tabs, and buttons are free to redesign.

Dear designers,

We've increased our budget and raise the prize money to 800 USD.  
We also accept the draft design in PNG format and we can go through the details in handover stage.
Thank you very much. 

Reason: Dear designers, We decided to extend the deadline by 7 days. As mentioned in the task description, we are looking for a new style of design and you might refer to the below style. A. 3D look & feel B. Realistic casino theme C. Richness and grandeur D. European casino style If you are still interested in our project, please send us your work. Thank you very much!

```html
<!DOCTYPE html>
<html lang="en">
<head>
<meta charset="utf-8">
<title>Live Casino Lobby</title>
<link href="https://fonts.googleapis.com/css2?family=Archivo:wght@700;800;900&family=Roboto:wght@400;700;900&display=swap" rel="stylesheet">
<style>
:root{
  --navy-900:#05062a;
  --navy-800:#0b0d3e;
  --navy-700:#16195a;
  --navy-600:#252a7a;
  --navy-500:#3a3f9a;
  --edge:#6d72c4;
  --gold:#f2c230;
  --gold-light:#ffe27a;
  --gold-dark:#b88a10;
  --felt:#0e4a4a;
  --felt-dark:#072a2c;
  --felt-line:#9fd8d0;
  --white:#ffffff;
  --grey:#a7a9c9;
  --red:#d21f2a;
  --blue:#2b3a9a;
  --grid:#c9c9d6;
  --page:#ffffff;
}
*{box-sizing:border-box;margin:0;padding:0}
html,body{width:1200px;height:1000px;overflow:hidden;background:var(--page);font-family:"Roboto",Arial,sans-serif;color:var(--white)}
.canvas{position:relative;width:1200px;height:1000px;overflow:hidden}
.lobby{position:absolute;left:130px;top:236px;width:942px;height:530px;background:radial-gradient(ellipse at 50% 40%,var(--navy-700),var(--navy-900) 75%);box-shadow:0 4px 14px rgba(0,0,0,.35);overflow:hidden}
.abs{position:absolute}

/* top bar */
.topbar{left:0;top:0;width:942px;height:30px;background:repeating-linear-gradient(90deg,var(--navy-900) 0 6px,var(--navy-600) 6px 9px);border-bottom:2px solid var(--grey)}
.topbar-base{left:0;top:0;width:300px;height:30px;background:var(--navy-900)}
.brand{left:8px;top:3px;display:flex;align-items:center;gap:6px;font-family:"Archivo",sans-serif;font-weight:800;font-size:21px;letter-spacing:.3px}
.brand-mark{width:18px;height:18px;border:2px solid var(--white);border-radius:50%}
.tools{right:10px;top:4px;display:flex;gap:4px}
.tool{width:22px;height:22px;background:var(--white);border-radius:3px;display:flex;align-items:center;justify-content:center}
.tool.close{background:var(--white)}

/* sidebar */
.sidebar{left:0;top:32px;width:140px;height:468px;background:linear-gradient(180deg,var(--navy-800),var(--navy-900))}
.clock{left:7px;top:12px;width:131px;height:20px;background:var(--navy-900);border:1px solid var(--navy-600);font-size:9px;font-weight:700;display:flex;align-items:center;justify-content:center}
.avatar-frame{left:16px;top:45px;width:113px;height:155px;border:2px solid var(--gold);border-radius:3px;background:var(--navy-800)}
.avatar{left:3px;top:3px;width:103px;height:125px;background:linear-gradient(180deg,#2b5c86,#16324f)}
.username{left:0;top:131px;width:109px;text-align:center;font-size:10px;font-weight:700;color:var(--grey)}
.profile-btn{left:16px;top:204px;width:112px;height:22px;border:2px solid var(--gold);border-radius:3px;background:var(--navy-900);font-size:8px;font-weight:700;color:var(--gold-light);display:flex;align-items:center;padding-left:10px;gap:8px}
.menu-item{left:16px;width:112px;height:20px;font-size:8px;font-weight:700;display:flex;align-items:center;gap:8px;padding-left:6px;background:linear-gradient(180deg,var(--navy-600),transparent);border-top:1px solid var(--navy-500)}
.coins{left:40px;top:394px;width:66px;height:64px;border-radius:50%;background:radial-gradient(circle,#f5cc3e,#a67710 60%,transparent 72%)}

/* tabs */
.tab{top:36px;height:32px;display:flex;align-items:center;gap:10px;font-family:"Archivo",sans-serif;font-weight:800;font-size:18px;letter-spacing:.5px;padding-left:16px}
.tab.active{left:150px;width:185px;border:2px solid var(--gold);border-radius:3px;background:linear-gradient(180deg,var(--navy-600),var(--navy-900));color:var(--gold-light);top:33px;height:35px;padding-left:42px}
.tab-icon{width:16px;height:16px;border-radius:50%}
.tab-sep{top:44px;width:1px;height:20px;background:var(--navy-500)}

/* dealers */
.featured{left:160px;top:76px;width:213px;height:102px;border-radius:3px;background:var(--navy-700);border-bottom:4px solid var(--gold)}
.portrait{background:linear-gradient(180deg,#22466e,#0c1d36);border:1px solid var(--edge)}
.roadmap{background:var(--white)}
.dealer-bar{left:6px;top:78px;width:202px;height:18px;background:var(--navy-900);font-size:10px;font-weight:700;display:flex;justify-content:space-between;align-items:center;padding-left:4px}
.deals-badge{background:var(--red);padding:1px 3px;border:1px solid var(--white)}
.others{left:385px;top:82px;width:535px;height:87px;border:3px solid var(--navy-500);border-radius:5px;background:var(--navy-800)}
.dealer-card{top:5px;width:165px;height:72px;background:var(--navy-700)}
.dealer-meta{left:6px;top:63px;width:153px;font-size:8px;font-weight:700;display:flex;justify-content:space-between}

/* main */
.main{left:156px;top:172px;width:780px;height:322px;border:3px solid var(--navy-600);border-radius:6px;background:var(--navy-800)}
.multiplayer{left:166px;top:184px;width:117px;height:36px;border:2px solid var(--gold);border-radius:3px;background:linear-gradient(180deg,var(--navy-600),var(--navy-900));font-size:11px;font-weight:700;color:var(--gold-light);display:flex;align-items:center;justify-content:center;gap:5px}
.multi-rail{left:290px;top:186px;width:220px;height:10px;background:var(--navy-600);border-radius:3px}
.filters{left:522px;top:191px;width:398px;height:20px;display:flex;background:var(--navy-600)}
.filter{flex:0 0 auto;height:20px;padding:0 8px;font-size:11px;font-weight:900;display:flex;align-items:center;border-right:1px solid var(--navy-900)}
.filter.join-any{color:var(--gold-light);padding:0 10px}
.scroll{left:917px;top:229px;width:15px;height:235px;background:var(--navy-900);border-radius:3px}
.scroll-thumb{left:1px;top:1px;width:13px;height:26px;border-radius:3px;background:linear-gradient(90deg,#6b4f8a,#b58ad0)}

.table-card{width:237px;height:117px;border:2px solid var(--gold);border-radius:3px;background:linear-gradient(180deg,var(--navy-700),var(--felt-dark))}
.tc-row{left:8px;right:8px;font-size:10px;font-weight:700;display:flex;justify-content:space-between}
.join{left:61px;top:19px;width:111px;height:38px;border-radius:50%;border:2px solid var(--grey);background:radial-gradient(ellipse at 50% 35%,var(--navy-500),var(--navy-900));font-family:"Archivo",sans-serif;font-style:italic;font-weight:800;font-size:19px;color:var(--gold-light);display:flex;align-items:center;justify-content:center}
.felt{left:0;top:44px}
.seats{left:4px;top:90px;width:227px;height:22px;display:flex;gap:4px}
.seat{width:30px;height:22px;display:flex;align-items:center;justify-content:center}
.seat-arrow{width:30px;height:20px;background:var(--navy-900);border-top:1px solid var(--edge);display:flex;align-items:center;justify-content:center}

/* footer */
.footer{left:0;top:500px;width:942px;height:30px;border-top:2px solid var(--grey);background:var(--navy-900)}
.balance{left:729px;top:3px;height:22px;display:flex;font-size:11px;font-weight:700}
.balance-label{width:60px;background:var(--red);display:flex;align-items:center;justify-content:center;border-radius:3px 0 0 3px}
.balance-cur{width:42px;background:#e6e6ee;color:#222;display:flex;align-items:center;justify-content:center}
.balance-amt{width:106px;background:var(--white);color:#222;display:flex;align-items:center;justify-content:center;border-radius:0 3px 3px 0}
</style>
</head>
<body>
<svg width="0" height="0" style="position:absolute">
  <defs>
    <symbol id="user" viewBox="0 0 20 20"><circle cx="10" cy="6" r="4.6" fill="#fff"/><path d="M2 20c0-6 3.5-8.5 8-8.5s8 2.5 8 8.5z" fill="#fff"/></symbol>
    <symbol id="down" viewBox="0 0 20 20"><path d="M7 2h6v8h4l-7 8-7-8h4z" fill="#fff"/></symbol>
    <pattern id="cells" width="8.5" height="8.5" patternUnits="userSpaceOnUse"><path d="M8.5 0V8.5H0" fill="none" stroke="#c9c9d6" stroke-width=".7"/></pattern>
    <symbol id="felt" viewBox="0 0 237 46">
      <polygon points="20,2 217,2 229,44 8,44" fill="#0e4a4a" stroke="#9fd8d0" stroke-width="1"/>
      <line x1="14" y1="23" x2="223" y2="23" stroke="#9fd8d0"/>
      <g stroke="#9fd8d0" stroke-width=".8">
        <line x1="48" y1="2" x2="40" y2="44"/><line x1="76" y1="2" x2="71" y2="44"/><line x1="104" y1="2" x2="103" y2="44"/>
        <line x1="133" y1="2" x2="134" y2="44"/><line x1="161" y1="2" x2="166" y2="44"/><line x1="189" y1="2" x2="197" y2="44"/>
      </g>
      <g font-family="Roboto,serif" font-style="italic" font-weight="700" font-size="10" text-anchor="middle">
        <g fill="#f2c230"><text x="33" y="17">B</text><text x="62" y="17">B</text><text x="90" y="17">B</text><text x="118" y="17">B</text><text x="147" y="17">B</text><text x="175" y="17">B</text><text x="204" y="17">B</text></g>
        <g fill="#ffffff"><text x="26" y="38">P</text><text x="56" y="38">P</text><text x="87" y="38">P</text><text x="118" y="38">P</text><text x="150" y="38">P</text><text x="181" y="38">P</text><text x="212" y="38">P</text></g>
      </g>
    </symbol>
  </defs>
</svg>

<div class="canvas">
<main class="lobby">

  <header class="abs topbar"></header>
  <div class="abs topbar-base"></div>
  <div class="abs brand"><span class="brand-mark"></span>LIVE CASINO</div>
  <nav class="abs tools">
    <span class="tool"><svg width="16" height="16" viewBox="0 0 16 16"><circle cx="8" cy="8" r="6.5" fill="none" stroke="#111" stroke-width="1.6"/><text x="8" y="11.5" font-size="9" font-weight="700" text-anchor="middle" fill="#111">$</text></svg></span>
    <span class="tool"><svg width="16" height="16" viewBox="0 0 16 16"><circle cx="8" cy="8" r="6.5" fill="none" stroke="#111" stroke-width="1.6"/><circle cx="7.5" cy="7.5" r="2.5" fill="none" stroke="#111" stroke-width="1.4"/><line x1="9.3" y1="9.3" x2="11.5" y2="11.5" stroke="#111" stroke-width="1.6"/></svg></span>
    <span class="tool"><svg width="16" height="16" viewBox="0 0 16 16"><path d="M6 3l7-1.5v9" fill="none" stroke="#111" stroke-width="1.6"/><path d="M6 3v9" stroke="#111" stroke-width="1.6"/><circle cx="4.5" cy="12" r="2" fill="#111"/><circle cx="11.5" cy="10.5" r="2" fill="#111"/></svg></span>
    <span class="tool"><svg width="16" height="16" viewBox="0 0 16 16"><g stroke="#111" stroke-width="1.8"><line x1="2" y1="2" x2="14" y2="14"/><line x1="14" y1="2" x2="2" y2="14"/></g><g fill="#111"><path d="M1 1h5L1 6z"/><path d="M15 1h-5l5 5z"/><path d="M1 15h5L1 10z"/><path d="M15 15h-5l5-5z"/></g></svg></span>
    <span class="tool close"><svg width="16" height="16" viewBox="0 0 16 16"><g stroke="#d21f2a" stroke-width="3"><line x1="3" y1="3" x2="13" y2="13"/><line x1="13" y1="3" x2="3" y2="13"/></g></svg></span>
  </nav>

  <aside class="abs sidebar">
    <div class="abs clock">1/28/2014 06:54 PM GMT + 8</div>
    <div class="abs avatar-frame">
      <div class="abs avatar" role="img" aria-label="Player avatar portrait"></div>
      <div class="abs username">ALPos848767</div>
    </div>
    <div class="abs profile-btn"><svg width="8" height="12" viewBox="0 0 8 12"><circle cx="4" cy="2.5" r="2.2" fill="#ffe27a"/><rect x="1.5" y="5" width="5" height="7" rx="1" fill="#ffe27a"/></svg>PROFILE</div>
    <div class="abs menu-item" style="top:246px"><svg width="10" height="9" viewBox="0 0 10 9"><path d="M0 3h3l5-3v9L3 6H0z" fill="#fff"/></svg>ANNOUNCEMENTS</div>
    <div class="abs menu-item" style="top:278px"><svg width="10" height="10" viewBox="0 0 10 10"><circle cx="5" cy="5" r="5" fill="#fff"/><rect x="4.2" y="4" width="1.6" height="4" fill="#0b0d3e"/><circle cx="5" cy="2.6" r=".9" fill="#0b0d3e"/></svg>RULES &amp; REGULATION</div>
    <div class="abs menu-item" style="top:311px"><svg width="10" height="10" viewBox="0 0 10 10"><circle cx="5" cy="5" r="4.2" fill="none" stroke="#fff" stroke-width="1.2"/><path d="M3 5l1.5 1.5L7 3.5" fill="none" stroke="#fff" stroke-width="1.2"/></svg>QUICK TOUR</div>
    <div class="abs coins" role="img" aria-label="Pile of gold coins"></div>
  </aside>

  <div class="abs tab active"><svg width="18" height="18" viewBox="0 0 18 18" style="position:absolute;left:40px"><rect x="2" y="3" width="9" height="13" rx="1" fill="#fff" transform="rotate(-12 6 9)"/><rect x="7" y="2" width="9" height="13" rx="1" fill="#fff" stroke="#0b0d3e"/></svg><span style="margin-left:26px">BACART</span></div>
  <div class="abs tab" style="left:350px"><span class="tab-icon" style="background:var(--red)"></span>SUPER SIX</div>
  <div class="abs tab-sep" style="left:520px"></div>
  <div class="abs tab" style="left:532px"><span class="tab-icon" style="width:20px;height:20px;background:radial-gradient(circle,#777 30%,#222 35%,#999 60%,#444)"></span>ROULETTE</div>
  <div class="abs tab-sep" style="left:712px"></div>
  <div class="abs tab" style="left:730px"><span class="tab-icon" style="border-radius:3px;background:var(--red)"></span>SIC BO</div>

  <section class="abs featured">
    <div class="abs portrait" style="left:7px;top:6px;width:68px;height:70px" role="img" aria-label="Dealer silhouette"></div>
    <svg class="abs" style="left:78px;top:8px" width="132" height="68">
      <rect width="132" height="68" fill="#fff"/><rect width="132" height="68" fill="url(#cells)"/>
      <g fill="none" stroke-width="1.6">
        <g stroke="#2b3a9a"><circle cx="4.3" cy="4.3" r="3.4"/><circle cx="4.3" cy="12.8" r="3.4"/><circle cx="21.3" cy="4.3" r="3.4"/><circle cx="29.8" cy="12.8" r="3.4"/><circle cx="55.3" cy="4.3" r="3.4"/><circle cx="89.3" cy="4.3" r="3.4"/><circle cx="89.3" cy="12.8" r="3.4"/><circle cx="89.3" cy="21.3" r="3.4"/><circle cx="97.8" cy="4.3" r="3.4"/><circle cx="106.3" cy="4.3" r="3.4"/><circle cx="106.3" cy="12.8" r="3.4"/><circle cx="114.8" cy="4.3" r="3.4"/><circle cx="114.8" cy="12.8" r="3.4"/><circle cx="114.8" cy="21.3" r="3.4"/></g>
        <g stroke="#d21f2a"><circle cx="12.8" cy="4.3" r="3.4"/><circle cx="29.8" cy="4.3" r="3.4"/><circle cx="38.3" cy="4.3" r="3.4"/><circle cx="46.8" cy="4.3" r="3.4"/><circle cx="63.8" cy="4.3" r="3.4"/><circle cx="72.3" cy="4.3" r="3.4"/><circle cx="80.8" cy="4.3" r="3.4"/><circle cx="97.8" cy="12.8" r="3.4"/><circle cx="97.8" cy="21.3" r="3.4"/><circle cx="97.8" cy="29.8" r="3.4"/><circle cx="97.8" cy="38.3" r="3.4"/><circle cx="97.8" cy="46.8" r="3.4"/></g>
      </g>
    </svg>
    <div class="abs dealer-bar"><span>Dealer Name</span><span class="deals-badge">Deals 999</span></div>
  </section>

  <section class="abs others">
    <div class="abs dealer-card" style="left:12px">
      <div class="abs portrait" style="left:3px;top:3px;width:52px;height:56px" role="img" aria-label="Dealer silhouette"></div>
      <svg class="abs" style="left:58px;top:2px" width="104" height="57"><rect width="104" height="57" fill="#fff"/><rect width="104" height="57" fill="url(#cells)"/><g fill="none" stroke-width="1.5"><g stroke="#2b3a9a"><circle cx="4.3" cy="4.3" r="3.3"/><circle cx="21.3" cy="4.3" r="3.3"/><circle cx="4.3" cy="12.8" r="3.3"/></g><g stroke="#d21f2a"><circle cx="12.8" cy="4.3" r="3.3"/><circle cx="29.8" cy="4.3" r="3.3"/><circle cx="12.8" cy="12.8" r="3.3"/></g></g></svg>
      <div class="abs dealer-meta"><span>Dealer Name</span><span>Deals 999</span></div>
    </div>
    <div class="abs dealer-card" style="left:184px">
      <div class="abs portrait" style="left:3px;top:3px;width:52px;height:56px" role="img" aria-label="Dealer silhouette"></div>
      <svg class="abs" style="left:58px;top:2px" width="104" height="57"><rect width="104" height="57" fill="#fff"/><rect width="104" height="57" fill="url(#cells)"/><g fill="none" stroke-width="1.5"><g stroke="#2b3a9a"><circle cx="4.3" cy="4.3" r="3.3"/><circle cx="4.3" cy="12.8" r="3.3"/><circle cx="4.3" cy="21.3" r="3.3"/><circle cx="21.3" cy="4.3" r="3.3"/></g><g stroke="#d21f2a"><circle cx="12.8" cy="4.3" r="3.3"/><circle cx="29.8" cy="4.3" r="3.3"/><circle cx="38.3" cy="4.3" r="3.3"/><circle cx="29.8" cy="12.8" r="3.3"/><circle cx="12.8" cy="12.8" r="3.3"/></g></g></svg>
      <div class="abs dealer-meta"><span>Dealer Name</span><span>Deals 999</span></div>
    </div>
    <div class="abs dealer-card" style="left:356px">
      <div class="abs portrait" style="left:3px;top:3px;width:52px;height:56px" role="img" aria-label="Dealer silhouette"></div>
      <svg class="abs" style="left:58px;top:2px" width="104" height="57"><rect width="104" height="57" fill="#fff"/><rect width="104" height="57" fill="url(#cells)"/><g fill="none" stroke-width="1.5"><g stroke="#2b3a9a"><circle cx="4.3" cy="4.3" r="3.3"/><circle cx="4.3" cy="12.8" r="3.3"/><circle cx="72.3" cy="12.8" r="3.3"/><circle cx="72.3" cy="21.3" r="3.3"/></g><g stroke="#d21f2a"><circle cx="12.8" cy="4.3" r="3.3"/><circle cx="21.3" cy="4.3" r="3.3"/><circle cx="29.8" cy="4.3" r="3.3"/><circle cx="38.3" cy="4.3" r="3.3"/><circle cx="72.3" cy="4.3" r="3.3"/></g></g></svg>
      <div class="abs dealer-meta"><span>Dealer Name</span><span>Deals 999</span></div>
    </div>
  </section>

  <section class="abs main"></section>
  <div class="abs multiplayer"><svg width="14" height="12" viewBox="0 0 20 16"><use href="#user" x="5" y="0" width="10" height="10"/><use href="#user" x="0" y="5" width="10" height="10"/><use href="#user" x="10" y="5" width="10" height="10"/></svg>MULTIPLAYER</div>
  <div class="abs multi-rail"></div>
  <div class="abs filters">
    <span class="filter join-any">JOIN ANY</span>
    <span class="filter">A↔Z</span>
    <span class="filter">$ ⬇</span>
    <span class="filter">$ ⬆</span>
    <span class="filter"><svg width="16" height="12" viewBox="0 0 20 16"><use href="#user" x="0" y="2" width="12" height="12"/><use href="#user" x="8" y="2" width="12" height="12"/></svg></span>
    <span class="filter">&lt; 3</span>
    <span class="filter">&gt; 3</span>
    <span class="filter" style="border:0">ALL Limits ▼</span>
  </div>
  <div class="abs scroll"><div class="abs scroll-thumb"></div></div>

  <!-- game tables -->
  <article class="abs table-card" style="left:167px;top:226px">
    <div class="abs tc-row" style="top:7px"><span>Baccarat A5 3C</span><span>Commission 07</span></div>
    <div class="abs tc-row" style="top:19px"><span>Bet Limit</span><span>0/100</span></div>
    <div class="abs join">JOIN</div>
    <svg class="abs felt" width="233" height="46"><use href="#felt" width="233" height="46"/></svg>
    <div class="abs seats"><span class="seat"><svg width="20" height="20"><use href="#user"/></svg></span><span class="seat"><svg width="20" height="20"><use href="#user"/></svg></span><span class="seat"><svg width="20" height="20"><use href="#user"/></svg></span><span class="seat"><svg width="20" height="20"><use href="#user"/></svg></span><span class="seat"><svg width="20" height="20"><use href="#user"/></svg></span><span class="seat-arrow"><svg width="16" height="16"><use href="#down"/></svg></span><span class="seat-arrow"><svg width="16" height="16"><use href="#down"/></svg></span></div>
  </article>
  <article class="abs table-card" style="left:417px;top:226px">
    <div class="abs tc-row" style="top:7px"><span>Baccarat A5 3C</span><span>Commission 07</span></div>
    <div class="abs tc-row" style="top:19px"><span>Bet Limit</span><span>0/100</span></div>
    <div class="abs join">JOIN</div>
    <svg class="abs felt" width="233" height="46"><use href="#felt" width="233" height="46"/></svg>
    <div class="abs seats"><span class="seat"><svg width="20" height="20"><use href="#user"/></svg></span><span class="seat"><svg width="20" height="20"><use href="#user"/></svg></span><span class="seat"><svg width="20" height="20"><use href="#user"/></svg></span><span class="seat"><svg width="20" height="20"><use href="#user"/></svg></span><span class="seat"><svg width="20" height="20"><use href="#user"/></svg></span><span class="seat-arrow"><svg width="16" height="16"><use href="#down"/></svg></span><span class="seat-arrow"><svg width="16" height="16"><use href="#down"/></svg></span></div>
  </article>
  <article class="abs table-card" style="left:667px;top:226px">
    <div class="abs tc-row" style="top:7px"><span>Baccarat A5 3C</span><span>Commission 07</span></div>
    <div class="abs tc-row" style="top:19px"><span>Bet Limit</span><span>0/100</span></div>
    <div class="abs join">JOIN</div>
    <svg class="abs felt" width="233" height="46"><use href="#felt" width="233" height="46"/></svg>
    <div class="abs seats"><span class="seat"><svg width="20" height="20"><use href="#user"/></svg></span><span class="seat"><svg width="20" height="20"><use href="#user"/></svg></span><span class="seat"><svg width="20" height="20"><use href="#user"/></svg></span><span class="seat"><svg width="20" height="20"><use href="#user"/></svg></span><span class="seat"><svg width="20" height="20"><use href="#user"/></svg></span><span class="seat-arrow"><svg width="16" height="16"><use href="#down"/></svg></span><span class="seat-arrow"><svg width="16" height="16"><use href="#down"/></svg></span></div>
  </article>
  <article class="abs table-card" style="left:167px;top:355px">
    <div class="abs tc-row" style="top:7px"><span>Baccarat A5 3C</span><span>Commission 07</span></div>
    <div class="abs tc-row" style="top:19px"><span>Bet Limit</span><span>0/100</span></div>
    <div class="abs join">JOIN</div>
    <svg class="abs felt" width="233" height="46"><use href="#felt" width="233" height="46"/></svg>
    <div class="abs seats"><span class="seat"><svg width="20" height="20"><use href="#user"/></svg></span><span class="seat"><svg width="20" height="20"><use href="#user"/></svg></span><span class="seat"><svg width="20" height="20"><use href="#user"/></svg></span><span class="seat"><svg width="20" height="20"><use href="#user"/></svg></span><span class="seat"><svg width="20" height="20"><use href="#user"/></svg></span><span class="seat-arrow"><svg width="16" height="16"><use href="#down"/></svg></span><span class="seat-arrow"><svg width="16" height="16"><use href="#down"/></svg></span></div>
  </article>
  <article class="abs table-card" style="left:417px;top:355px">
    <div class="abs tc-row" style="top:7px"><span>Baccarat A5 3C</span><span>Commission 07</span></div>
    <div class="abs tc-row" style="top:19px"><span>Bet Limit</span><span>0/100</span></div>
    <div class="abs join">JOIN</div>
    <svg class="abs felt" width="233" height="46"><use href="#felt" width="233" height="46"/></svg>
    <div class="abs seats"><span class="seat"><svg width="20" height="20"><use href="#user"/></svg></span><span class="seat"><svg width="20" height="20"><use href="#user"/></svg></span><span class="seat"><svg width="20" height="20"><use href="#user"/></svg></span><span class="seat"><svg width="20" height="20"><use href="#user"/></svg></span><span class="seat"><svg width="20" height="20"><use href="#user"/></svg></span><span class="seat-arrow"><svg width="16" height="16"><use href="#down"/></svg></span><span class="seat-arrow"><svg width="16" height="16"><use href="#down"/></svg></span></div>
  </article>
  <article class="abs table-card" style="left:667px;top:355px">
    <div class="abs tc-row" style="top:7px"><span>Baccarat A5 3C</span><span>Commission 07</span></div>
    <div class="abs tc-row" style="top:19px"><span>Bet Limit</span><span>0/100</span></div>
    <div class="abs join">JOIN</div>
    <svg class="abs felt" width="233" height="46"><use href="#felt" width="233" height="46"/></svg>
    <div class="abs seats"><span class="seat"><svg width="20" height="20"><use href="#user"/></svg></span><span class="seat"><svg width="20" height="20"><use href="#user"/></svg></span><span class="seat"><svg width="20" height="20"><use href="#user"/></svg></span><span class="seat"><svg width="20" height="20"><use href="#user"/></svg></span><span class="seat"><svg width="20" height="20"><use href="#user"/></svg></span><span class="seat-arrow"><svg width="16" height="16"><use href="#down"/></svg></span><span class="seat-arrow"><svg width="16" height="16"><use href="#down"/></svg></span></div>
  </article>

  <footer class="abs footer">
    <div class="abs balance"><span class="balance-label">Balance</span><span class="balance-cur">$SGD</span><span class="balance-amt">999,999.999</span></div>
  </footer>

</main>
</div>
</body>
</html>
```